Medical Education and Learning Portal refresh

We at Vantrel Limited have developed a learning platform for medical students. It is based around multiple choice questions, but has social and gaming elements built in to make it fun. It will be used on desktop and mobile devices.

I am looking for a refresh of the 'dated' design into something modern and transferrable between devices.

Note that I have a 'focus group' of Medical Students on 4 February where the Top 3-4 designs will be shown to them for them to pick the winner.

I have also uploaded screenshots of the current site. Essentially I would like to reduce the complexity of design into 2-3 pages (currently unlogged in front/home page, logged in page with options, answer questions page, competition page, revision page/summary pages etc). What I am really after is a good clean colour scheme & structure.

If we get the design colour scheme right then I can pay additionally for coding and maybe some additional structure to pages.
Updates

Target Market(s)

Healthcare/Medical Students

Industry/Entity Type

Healthcare

Number of Pages Required

4 page

Font styles to use
Serif
Sans Serif

Requirements
Must have
• 'Clean' Web 2.0 (or later) feel to it.
• I also expect that the images for the trophies are 'cleaned up (each trophy has a bronze/silver/platinum version as users increase their score. I am looking for these to be clean and simple but fun!
• I also need the final design to be transferrable from a desktop browser to a mobile device. I will need designs for home page/content page/Q&A page.
• I previously had a side panel float over the site but that is dated now and I would like to have a page with each element clearly on it and any information would briefly float over this but not take the focus away from the main function of the page.
• I have included the 'bronze', 'silver', 'gold' trophy icons in the files. These are fine in one sense but ideally the colours will blend well too ...
• The following article summarises my must haves:
• http://plumquarry-notes.example/web-design/layout-trend-field-guide/
Nice to have
• Creative concept for presenting MCQ's to students, with a timer and box of information about the question (level of the question, the percent of student who get it right ... etc).
Should not have
• Too much complexity ... clean with a few colours is what I am after
• Note too that my logo is not changing and the colours should blend with this.

```html
<!DOCTYPE html>
<html lang="en">
<head>
<meta charset="utf-8">
<title>Vantrel – Medical Education and Learning Platform</title>
<link rel="stylesheet" href="https://fonts.googleapis.com/css2?family=Cantarell:wght@400;700&family=Open+Sans:wght@400;600;700&display=swap">
<style>
:root{
  --blue:#1a78b6;
  --blue-dark:#0d64a0;
  --navy:#123a56;
  --ink:#1f3346;
  --text:#555d66;
  --orange:#f28a0f;
  --grey-bg:#f4f4f4;
  --footer-bg:#fafafa;
  --bar-bg:#e6e6e6;
  --line:#d5d8db;
  --white:#ffffff;
}
*{box-sizing:border-box;margin:0;padding:0}
html,body{width:773px;height:1200px;overflow:hidden;background:var(--white)}
body{position:relative;font-family:"Open Sans",sans-serif;color:var(--text)}
.abs{position:absolute}
.heading{font-family:"Cantarell",sans-serif}

/* header */
.top-strip{left:0;top:0;width:773px;height:4px;background:var(--navy)}
.brand{left:134px;top:14px}
.brand-name{font-family:"Cantarell",sans-serif;font-size:22px;color:var(--blue);line-height:1}
.brand-tag{font-size:6px;font-weight:700;color:var(--ink);margin-top:4px}
.field{height:14px;border:1px solid #c9ccd0;border-radius:8px;font-size:5.5px;color:#9aa;padding:3px 7px;background:#fff}
.btn{height:14px;border-radius:8px;font-size:5.5px;font-weight:700;color:#fff;text-align:center;line-height:14px;letter-spacing:.3px}
.btn-blue{background:var(--blue)}
.btn-orange{background:var(--orange)}
.social{display:flex;gap:3px}
.social span{width:14px;height:14px;border-radius:50%;background:#8d9296}
.social span.on{background:var(--blue)}

/* nav */
.nav{left:0;top:56px;width:773px;height:37px;background:var(--blue)}
.nav-list{position:absolute;left:134px;top:0;display:flex;list-style:none}
.nav-item{width:101px;height:37px;color:#fff;font-size:6.5px;font-weight:600;text-align:center;border-right:1px solid rgba(255,255,255,.18);padding-top:8px}
.nav-item svg{display:block;margin:0 auto 3px}
.nav-item.active{background:var(--orange)}

/* hero */
.hero{left:0;top:93px;width:773px;height:249px;background:linear-gradient(90deg,#d7ecf7 0%,#bfe0f1 35%,#a6d0e8 55%,#d9c4b1 75%,#8fc2e0 100%)}
.hero-title{left:134px;top:160px;font-size:16px;color:var(--ink);line-height:20px}
.hero-points{left:134px;top:206px;list-style:none;font-size:9.5px;color:#4a5560;line-height:13.5px}
.hero-points li{display:flex;align-items:center;gap:5px}
.hero-cta{left:134px;top:259px;width:82px;height:19px;border-radius:10px;background:var(--blue);color:#fff;font-size:7.5px;font-weight:600;text-align:center;line-height:19px}

/* how it works */
.how-title{left:0;width:773px;top:375px;text-align:center;font-size:15px;color:var(--ink)}
.how-sub{left:0;width:773px;top:393px;text-align:center;font-size:7px;color:#444}
.frame{background:#f5f5f5;border:1px solid #9ea3a8;border-bottom:none;border-radius:6px 6px 0 0}
.screen{background:linear-gradient(135deg,#c9a78a 0%,#7d6652 45%,#e8e4df 60%,#2b2b2b 100%)}

/* about + tweets */
.about-bg{left:0;top:565px;width:393px;height:273px;background:var(--grey-bg)}
.tweets-bg{left:685px;top:565px;width:88px;height:273px;background:var(--grey-bg)}
.about-title{left:134px;top:601px;font-size:15px;color:var(--blue)}
.about-sub{left:134px;top:620px;font-size:7px;color:var(--blue)}
.about-rule{left:120px;top:637px;width:259px;height:1px;background:var(--line)}
.about-copy{left:134px;top:649px;width:232px;font-size:6.4px;line-height:9.3px;color:#4e5257}
.about-copy p+p{margin-top:9px}
.read-more{left:134px;top:788px;font-size:7px;color:var(--blue);display:flex;align-items:center;gap:3px}
.tweets{left:436px;top:601px;width:202px;height:200px;border:1px solid #cfd3d6;border-radius:2px;background:#fff}
.tweets-head{height:36px;border-bottom:1px solid #dde0e2;padding:12px 9px;font-family:"Cantarell",sans-serif;font-size:10px;color:var(--ink);font-weight:700;display:flex;justify-content:space-between}
.follow{font-family:"Open Sans",sans-serif;font-size:5px;border:1px solid #ccc;border-radius:2px;padding:1px 4px;height:9px;color:#333;font-weight:600}
.tweet{display:flex;gap:8px;padding:8px 9px;height:49px;border-bottom:1px solid #eceeef;font-size:5.5px;line-height:8px;color:#333;width:196px}
.tweet:last-child{border-bottom:none}
.avatar{width:22px;height:22px;border-radius:3px;background:#3d4348;flex:none}
.tweet b{font-size:6px}
.handle{color:#999}
.tag{color:var(--blue)}
.scroll{right:1px;top:37px;width:6px;height:161px;background:#f0f0f0}

/* newsletter / question */
.news-band{left:0;top:838px;width:393px;height:121px;background:var(--blue)}
.ask-band{left:393px;top:838px;width:380px;height:121px;background:var(--blue-dark)}
.band-title{font-size:13px;color:#fff;letter-spacing:.4px}
.band-copy{font-size:6.5px;color:#e2eef7;line-height:9px}
.news-input{left:134px;top:904px;width:202px;height:14px;border-radius:8px;background:#fff;font-size:5.5px;color:#999;padding:3px 9px}
.news-btn{left:266px;top:904px;width:70px;height:14px;border-radius:8px;background:var(--navy);color:#fff;font-size:5.5px;font-weight:700;text-align:center;line-height:14px;letter-spacing:.5px}
.privacy{left:134px;top:929px;font-size:7px;color:#fff;text-decoration:underline;display:flex;align-items:center;gap:3px}

/* footer */
.footer{left:0;top:959px;width:773px;height:193px;background:var(--footer-bg)}
.foot-head{top:993px;font-size:7px;font-weight:700;color:var(--ink);letter-spacing:.4px}
.foot-links{top:1013px;list-style:none;font-size:6.5px;line-height:12.8px;color:#666}
.foot-links .hot{color:var(--orange)}
.foot-divider{left:394px;top:984px;width:1px;height:152px;background:#e0e2e4}
.contact{left:436px;top:1013px;font-size:6.5px;line-height:8.6px;color:#555}
.contact p{margin-bottom:8px}
.bar{left:0;top:1152px;width:773px;height:48px;background:var(--bar-bg)}
.bar-brand{left:136px;top:1163px;font-family:"Cantarell",sans-serif;font-size:14px;color:#333}
.copyright{left:220px;top:1169px;font-size:6.5px;color:#333}
.back-top{left:592px;top:1169px;font-size:6.5px;color:#333;display:flex;align-items:center;gap:3px}
</style>
</head>
<body>

<div class="abs top-strip"></div>

<header>
  <div class="abs brand">
    <div class="brand-name">Vantrel</div>
    <div class="brand-tag">The Medical Peer Review</div>
  </div>
  <div class="abs field" style="left:264px;top:25px;width:101px">Email</div>
  <div class="abs field" style="left:370px;top:25px;width:112px">Password</div>
  <div class="abs btn btn-blue" style="left:446px;top:25px;width:44px">LOGIN</div>
  <div class="abs btn btn-orange" style="left:495px;top:25px;width:59px">FREE SIGN UP</div>
  <div class="abs social" style="left:572px;top:25px"><span></span><span class="on"></span><span></span><span></span></div>
</header>

<nav class="abs nav">
  <ul class="nav-list">
    <li class="nav-item active"><svg width="11" height="10" viewBox="0 0 11 10"><path d="M5.5 0L0 5h1.5v5h3V7h2v3h3V5H11z" fill="#fff"/></svg>Home</li>
    <li class="nav-item"><svg width="11" height="10" viewBox="0 0 11 10"><rect x="1" y="3" width="9" height="6.5" rx="1" fill="none" stroke="#fff" stroke-width="1.2"/><path d="M3.5 0.5L5.5 3L7.5 0.5" fill="none" stroke="#fff" stroke-width="1"/></svg>Take the Tour</li>
    <li class="nav-item"><svg width="16" height="10" viewBox="0 0 16 10"><circle cx="8" cy="2.5" r="2.3" fill="#fff"/><circle cx="3" cy="3.5" r="1.8" fill="#fff"/><circle cx="13" cy="3.5" r="1.8" fill="#fff"/><path d="M4 10a4 4 0 0 1 8 0zM0 10a3 3 0 0 1 5-2.5L4 10zM16 10a3 3 0 0 0-5-2.5l1 2.5z" fill="#fff"/></svg>What Your Preers Say</li>
    <li class="nav-item"><svg width="11" height="10" viewBox="0 0 11 10"><path d="M5.5 0l1.6 3.4 3.7.4-2.8 2.5.8 3.7-3.3-1.9-3.3 1.9.8-3.7L.2 3.8l3.7-.4z" fill="#fff"/></svg>Subscription Plan</li>
    <li class="nav-item" style="border-right:none"><svg width="11" height="10" viewBox="0 0 11 10"><rect x="3" y="0.5" width="5" height="9" rx="1" fill="none" stroke="#fff" stroke-width="1.2"/></svg>Contact Us</li>
  </ul>
</nav>

<section>
  <div class="abs hero" role="img" aria-label="Photo of three smiling medical professionals reviewing work together in a bright glass office"></div>
  <h1 class="abs heading hero-title" style="font-weight:400">Vantrel - Medical Education and<br>Learning Platform</h1>
  <ul class="abs hero-points">
    <li><svg width="9" height="9" viewBox="0 0 9 9"><rect x=".6" y=".6" width="7.8" height="7.8" rx="1" fill="none" stroke="#f28a0f" stroke-width="1.2"/><path d="M2 4.5l2 2 4-5" fill="none" stroke="#f28a0f" stroke-width="1.4"/></svg>Know your registered friends progress.</li>
    <li><svg width="9" height="9" viewBox="0 0 9 9"><rect x=".6" y=".6" width="7.8" height="7.8" rx="1" fill="none" stroke="#f28a0f" stroke-width="1.2"/><path d="M2 4.5l2 2 4-5" fill="none" stroke="#f28a0f" stroke-width="1.4"/></svg>Earn trophies with increased knowledge.</li>
    <li><svg width="9" height="9" viewBox="0 0 9 9"><rect x=".6" y=".6" width="7.8" height="7.8" rx="1" fill="none" stroke="#f28a0f" stroke-width="1.2"/><path d="M2 4.5l2 2 4-5" fill="none" stroke="#f28a0f" stroke-width="1.4"/></svg>29.903 Questions answered.</li>
  </ul>
  <div class="abs hero-cta">Get Started Now</div>
</section>

<section>
  <h2 class="abs heading how-title" style="font-weight:400">How it Work?</h2>
  <p class="abs how-sub">Take a Tour of our Platform now with Video !</p>

  <div class="abs frame" style="left:186px;top:474px;width:78px;height:91px"></div>
  <div class="abs screen" style="left:193px;top:481px;width:71px;height:84px" role="img" aria-label="Video still of hands playing a piano"></div>
  <svg class="abs" style="left:223px;top:516px" width="16" height="14" viewBox="0 0 16 14"><path d="M15 7H2M7 1L1 7l6 6" fill="none" stroke="#fff" stroke-width="1.6"/></svg>

  <div class="abs frame" style="left:509px;top:474px;width:77px;height:91px"></div>
  <div class="abs screen" style="left:509px;top:481px;width:70px;height:84px" role="img" aria-label="Video still of hands playing a piano"></div>
  <svg class="abs" style="left:536px;top:516px" width="16" height="14" viewBox="0 0 16 14"><path d="M1 7h13M9 1l6 6-6 6" fill="none" stroke="#e8e8e8" stroke-width="1.6"/></svg>

  <div class="abs frame" style="left:265px;top:420px;width:243px;height:145px;background:#fafafa"></div>
  <div class="abs" style="left:385px;top:425px;width:3px;height:3px;border-radius:50%;background:#333"></div>
  <div class="abs screen" style="left:275px;top:431px;width:222px;height:134px" role="img" aria-label="Tour video still of hands playing a piano"></div>
  <svg class="abs" style="left:369px;top:481px" width="36" height="36" viewBox="0 0 36 36"><circle cx="18" cy="18" r="17" fill="rgba(255,255,255,.85)"/><path d="M14 10l12 8-12 8z" fill="#555"/></svg>
</section>

<section>
  <div class="abs about-bg"></div>
  <div class="abs tweets-bg"></div>
  <h2 class="abs heading about-title" style="font-weight:400">Vantrel</h2>
  <p class="abs about-sub">Medical Education and Learning Platform</p>
  <div class="abs about-rule"></div>
  <div class="abs about-copy">
    <p>Lorem Ipsum is simply dummy text of the printing and typesetting industry. Lorem Ipsum has been the industry's standard dummy text ever since the 1500s, when an unknown printer took a galley of type and scrambled it to make a type specimen book.</p>
    <p>It is a long established fact that a reader will be distracted by the readable content of a page when looking at its layout. The point of using Lorem Ipsum is that it has a more-or-less normal distribution of letters, as opposed to using 'Content here, content here', making it look like readable English. Many desktop publishing packages and web page editors now use Lorem Ipsum as their default model text, and a search for 'lorem ipsum' will uncover many web sites still in their infancy. Various versions have evolved over the years,...</p>
  </div>
  <div class="abs read-more"><svg width="7" height="7" viewBox="0 0 7 7"><circle cx="3.5" cy="3.5" r="3.5" fill="#1a78b6"/><path d="M2 3.5h3M3.6 2l1.5 1.5-1.5 1.5" fill="none" stroke="#fff" stroke-width=".9"/></svg>Read More</div>

  <div class="abs tweets">
    <div class="tweets-head">Posts <span class="follow">Follow</span></div>
    <div class="tweet"><div class="avatar"></div><div><b>Chirpnet</b> <span class="handle">@chirpnet</span> <span class="handle" style="float:right">8 Sep</span><br>#fbf to my fav moment building a school in Nepal with strong, humble Tharu women. <span class="tag">@raiseSchools</span><br><span class="tag">#nepal #education #women</span></div></div>
    <div class="tweet"><div class="avatar"></div><div><b>Chirpnet</b> <span class="handle">@chirpnet</span> <span class="handle" style="float:right">8 Sep</span><br>#fbf to my fav moment building a school in Nepal with strong, humble Tharu women. <span class="tag">@raiseSchools</span><br><span class="tag">#nepal #education #women</span></div></div>
    <div class="tweet"><div class="avatar"></div><div><b>Chirpnet</b> <span class="handle">@chirpnet</span> <span class="handle" style="float:right">8 Sep</span><br>#fbf to my fav moment building a school in Nepal with strong, humble Tharu women. <span class="tag">@raiseSchools</span><br><span class="tag">#nepal #education #women</span><br><span class="handle">Reposted by Chirpnet</span></div></div>
    <div class="abs scroll"></div>
  </div>
</section>

<section>
  <div class="abs news-band"></div>
  <div class="abs ask-band"></div>
  <h3 class="abs heading band-title" style="left:134px;top:857px;font-weight:400">Newsletter</h3>
  <p class="abs band-copy" style="left:134px;top:876px;width:220px">Sign up for email and text updates to get deadline reminders and other important information.</p>
  <div class="abs news-input">Enter Your Email</div>
  <div class="abs news-btn">SIGN UP</div>
  <div class="abs privacy"><svg width="7" height="7" viewBox="0 0 7 7"><circle cx="3.5" cy="3.5" r="3.5" fill="#fff"/><path d="M2 3.5h3M3.6 2l1.5 1.5-1.5 1.5" fill="none" stroke="#1a78b6" stroke-width=".9"/></svg>Provacy Policy</div>

  <h3 class="abs heading band-title" style="left:437px;top:857px;font-weight:400;display:flex;align-items:center;gap:4px"><svg width="14" height="14" viewBox="0 0 14 14"><circle cx="7" cy="7" r="7" fill="#fff"/><path d="M5 5.2a2 2 0 1 1 2.6 1.9c-.5.2-.6.5-.6 1.2" fill="none" stroke="#0d64a0" stroke-width="1.5"/><circle cx="7" cy="10.5" r=".9" fill="#0d64a0"/></svg>Post Your Question ?</h3>
  <p class="abs band-copy" style="left:437px;top:876px;width:185px">Do you have any unique Questions for which looking for Answers?</p>
  <div class="abs btn btn-orange" style="left:433px;top:904px;width:63px">POST NOW</div>
</section>

<footer>
  <div class="abs footer"></div>
  <h4 class="abs foot-head" style="left:134px">RESOURCES</h4>
  <ul class="abs foot-links" style="left:134px">
    <li>Take the Tour</li><li class="hot">What your Preers Say</li><li>Subcription Plan</li><li>Friends</li><li>Moderation</li><li>Statistics</li><li>Competition</li><li>Answer Question</li><li>Post Question</li>
  </ul>
  <h4 class="abs foot-head" style="left:263px">QUICK LINK</h4>
  <ul class="abs foot-links" style="left:263px">
    <li>Home</li><li>About</li><li>Contact Us</li><li>Privacy Policy</li><li>T &amp; C's</li><li>Site Map</li>
  </ul>
  <div class="abs foot-divider"></div>
  <h4 class="abs foot-head" style="left:436px">CONNECT WITH US</h4>
  <div class="abs contact">
    <p>Vantrel Limited<br>48 Harrow Lane #12 Dunmore, Ma 02190</p>
    <p>Phone<br>+1 555 014 2277</p>
    <p>Email<br>support@vantrellimited.example</p>
  </div>
  <div class="abs social" style="left:436px;top:1098px"><span></span><span></span><span></span><span></span></div>

  <div class="abs bar"></div>
  <div class="abs bar-brand">Vantrel</div>
  <p class="abs copyright">© 2016 Vantrel Limited . All Rights Reserved</p>
  <div class="abs back-top"><svg width="7" height="8" viewBox="0 0 7 8"><path d="M3.5 8V1M.5 4l3-3 3 3" fill="none" stroke="#1a78b6" stroke-width="1.4"/></svg>Back to Top</div>
</footer>

</body>
</html>
```